Commercial construction contractor website.

We need a website that contains About Us, Contact info, Services, Project pictures and Industry News section

Target Market(s)

I'm building industral/flex spaces/commercial.

Industry/Entity Type

Commercial/industrial construction

Coding

Coded - Design and coding required

Number of Pages Required

5+ page

Font styles to use
Other font styles liked:
• The logo font is Microgramma Pro

Requirements
Must have
• Must have correct company name spelling: Dunmore Ridge Construction
Nice to have
• I do like to see our logo design implemented in the design
Should not have
• Please do not show big city pictures and business suit people. We are a commercial construction company

```html
<!DOCTYPE html>
<html lang="en">
<head>
<meta charset="utf-8">
<title>Dunmore Ridge Construction</title>
<link href="https://fonts.googleapis.com/css2?family=Poppins:wght@400;500;600;700&display=swap" rel="stylesheet">
<style>
:root{
  --blue:#0a82c4;
  --blue-dark:#06609a;
  --ink:#111;
  --muted:#8a8a8a;
  --backdrop:#f1f1f1;
  --white:#fff;
  --black:#000;
  --line:#e6e6e6;
}
*{box-sizing:border-box;margin:0;padding:0}
html,body{width:1200px;height:1200px;overflow:hidden;background:var(--backdrop);font-family:'Poppins',sans-serif;color:var(--ink)}
.stage{position:absolute;left:0;top:0;width:1932px;height:1932px;transform:scale(0.62112);transform-origin:0 0}
.page{position:absolute;left:688px;top:0;width:556px;height:1932px;background:var(--white);overflow:hidden;box-shadow:0 0 12px rgba(0,0,0,.06)}
.abs{position:absolute}
.brand{left:64px;top:6px;width:100px;text-align:center;color:var(--blue-dark);font-size:6px;font-weight:600;letter-spacing:.3px}
.brand .dot{display:block;width:18px;height:18px;border-radius:50%;background:var(--blue-dark);margin:0 auto 4px}
.hero-photo{left:286px;top:0;width:270px;height:324px;border-bottom-left-radius:100% 100%;background:linear-gradient(160deg,#3aa7e4 0%,#1f6fb3 45%,#8d6a4f 85%,#a07c5d 100%)}
.nav{left:302px;top:15px;display:flex;gap:9px;font-size:7px;color:var(--white)}
.hero-title{left:52px;top:98px;font-size:20.5px;line-height:24px;font-weight:700;color:var(--blue)}
.hero-text{left:52px;top:154px;width:220px;font-size:7px;line-height:11px;color:#555}
.btn{background:var(--blue);color:var(--white);font-size:7px;font-weight:700;display:flex;align-items:center;justify-content:center;border-radius:3px;width:122px;height:32px;box-shadow:0 4px 8px rgba(10,130,196,.25)}
.section-title{left:0;width:556px;text-align:center;font-size:14px;font-weight:600}
.card{background:var(--white);box-shadow:0 2px 10px rgba(0,0,0,.08);text-align:center}
.card-img{height:94px}
.card h3{font-size:9px;font-weight:600;margin-top:17px}
.card p{font-size:6.2px;line-height:10.5px;color:var(--muted);padding:4px 4px 0}
.card .more{font-size:5.5px;font-weight:700;margin-top:4px}
.card.active{background:var(--blue);color:var(--white)}
.card.active p{color:#dceefa}
.service-photo{left:0;top:586px;width:262px;height:514px;border-radius:0 100% 100% 0 / 0 50% 50% 0;background:linear-gradient(180deg,#8fc2e6 0%,#4a8fc6 40%,#1d4f84 100%)}
.svc-title{left:277px;top:697px;font-size:14.5px;font-weight:600}
.svc{width:110px}
.svc .ic{width:21px;height:21px;border-radius:50%;background:var(--blue);display:flex;align-items:center;justify-content:center}
.svc h4{font-size:9px;font-weight:500;margin-top:10px}
.svc p{font-size:6px;line-height:10px;color:var(--muted);margin-top:4px}
.band{left:0;top:1124px;width:556px;height:250px;background:var(--blue)}
.band-title{color:var(--white);top:1146px}
.tcard{background:var(--white);width:150px;height:142px;top:1181px;text-align:center;border-radius:2px}
.avatar{width:40px;height:40px;border-radius:50%;background:linear-gradient(#cfd4d9,#8b9097);margin:24px auto 0}
.tcard h4{font-size:9px;font-weight:500;margin-top:10px}
.tcard p{font-size:6.2px;line-height:10px;color:var(--muted);padding:5px 6px 0}
.dots{left:0;width:556px;top:1344px;display:flex;gap:7px;justify-content:center}
.dots i{width:5px;height:5px;border-radius:50%;background:#cfe7f6}
.dots i.on{background:var(--white)}
.proj{top:1426px;width:106px;height:134px;border-radius:2px}
.contact-title{left:52px;top:1574px;font-size:15px;font-weight:600}
.label{font-size:7px;font-weight:500}
.label b{color:var(--blue);font-weight:500}
.field{border:1px solid var(--line);box-shadow:0 2px 6px rgba(0,0,0,.05);font-size:7px;color:var(--muted);padding:12px 11px;border-radius:2px}
.map{left:379px;top:1579px;width:125px;height:166px;background:linear-gradient(135deg,#dfeaf6,#bfd4ea)}
.footer{left:0;top:1812px;width:556px;height:120px;background:var(--black);color:var(--white)}
.vline{top:0;width:1px;height:120px;background:#333}
.f-brand{left:62px;top:40px;width:96px;text-align:center;font-size:6px;color:var(--blue);font-weight:600}
.f-brand .dot{display:block;width:28px;height:28px;border-radius:50%;background:var(--blue);margin:0 auto 6px}
.f-head{font-size:11.5px;font-weight:500}
.f-small{font-size:4.8px;line-height:8px}
.f-row{display:flex;align-items:center;gap:5px}
.f-row .pin{width:8px;height:8px;border-radius:50%;background:var(--white);flex:none}
.links{font-size:5px;text-align:center;line-height:14.5px;width:70px}
.socials{display:flex;gap:4px;margin-top:4px}
.socials i{width:10px;height:10px;border-radius:50%;background:var(--white)}
</style>
</head>
<body>
<div class="stage">
<main class="page">

  <header>
    <div class="abs brand"><span class="dot"></span>DUNMORE RIDGE</div>
    <div class="abs hero-photo" role="img" aria-label="Two site workers in hard hats and safety vests looking at a steel frame structure"></div>
    <nav class="abs nav"><span>Home</span><span>About Us</span><span>Service</span><span>Contact Us</span><span>Project View</span></nav>
    <h1 class="abs hero-title">BUILD STRONG<br>BUILD YOUR QUALITY</h1>
    <p class="abs hero-text">Lorem Ipsum is simply dummy text of the printing and typesetting industry. Lorem Ipsum has been the industry's</p>
    <a class="abs btn" style="left:52px;top:188px">GET IN TOUCH</a>
  </header>

  <section>
    <h2 class="abs section-title" style="top:344px">About Us</h2>
    <article class="abs card" style="left:52px;top:377px;width:139px;height:188px">
      <div class="card-img" role="img" aria-label="Modern building exterior under a blue sky" style="background:linear-gradient(#3a8de0,#6f8d9a)"></div>
      <h3>Western Buildes</h3>
      <p>Lorem ipsum dolor sit amet, consectetur adipiscing elit, sed do eiusmod tempor incididunt ut labore et dolore.</p>
      <div class="more">EXPLORE MORE &rsaquo;</div>
    </article>
    <article class="abs card active" style="left:208px;top:375px;width:140px;height:190px">
      <div class="card-img" role="img" aria-label="Contemporary two-storey house with timber cladding" style="background:linear-gradient(#9bb3c6,#6b5a48)"></div>
      <h3>Redinex</h3>
      <p>Lorem ipsum dolor sit amet, consectetur adipiscing elit, sed do eiusmod tempor incididunt ut labore et dolore.</p>
      <div class="more">EXPLORE MORE &rsaquo;</div>
    </article>
    <article class="abs card" style="left:366px;top:376px;width:138px;height:189px">
      <div class="card-img" role="img" aria-label="Lit villa with a pool at dusk" style="background:linear-gradient(#1d3f9a,#3d7fd0)"></div>
      <h3>Front Home</h3>
      <p>Lorem ipsum dolor sit amet, consectetur adipiscing elit, sed do eiusmod tempor incididunt ut labore et dolore.</p>
      <div class="more">EXPLORE MORE &rsaquo;</div>
    </article>
  </section>

  <section>
    <div class="abs service-photo" role="img" aria-label="Blue-toned apartment block with balconies and antennas"></div>
    <h2 class="abs svc-title">Our Service</h2>
    <div class="abs svc" style="left:277px;top:724px"><div class="ic"><svg width="10" height="10" viewBox="0 0 10 10"><path d="M5 1l3 1v3c0 2-1.5 3-3 4C3.5 8 2 7 2 5V2z" fill="#fff"/></svg></div><h4>Safety</h4><p>Lorem ipsum dolor sit amet, etur adipiscing elit, sed do eiusmpor.</p></div>
    <div class="abs svc" style="left:398px;top:724px"><div class="ic"><svg width="10" height="10" viewBox="0 0 10 10"><path d="M2 8h6M5 2v6" stroke="#fff" stroke-width="1.2"/></svg></div><h4>Site Challenges</h4><p>Lorem ipsum dolor sit amet, etur adipiscing elit,</p></div>
    <div class="abs svc" style="left:277px;top:799px"><div class="ic"><svg width="10" height="10" viewBox="0 0 10 10"><circle cx="5" cy="5.5" r="3" fill="none" stroke="#fff" stroke-width="1.2"/><path d="M5 5.5V4" stroke="#fff"/></svg></div><h4>Uninterrupted Prod</h4><p>Lorem ipsum dolor sit amet, etur adipiscing elit, sed do eiusmpor.</p></div>
    <div class="abs svc" style="left:398px;top:799px"><div class="ic"><svg width="10" height="10" viewBox="0 0 10 10"><rect x="2" y="3" width="6" height="5" fill="none" stroke="#fff"/></svg></div><h4>Logistic Challenges</h4><p>Lorem ipsum dolor sit amet, etur adipiscing elit,</p></div>
    <div class="abs svc" style="left:277px;top:874px"><div class="ic"><svg width="10" height="10" viewBox="0 0 10 10"><path d="M2.5 5a2.5 2.5 0 0 1 5 0M7.5 5a2.5 2.5 0 0 1-5 0" fill="none" stroke="#fff" stroke-width="1.2"/></svg></div><h4>Unique Materials</h4><p>Lorem ipsum dolor sit amet, etur adipiscing elit, sed do eiusmpor.</p></div>
    <div class="abs svc" style="left:398px;top:874px"><div class="ic"><svg width="10" height="10" viewBox="0 0 10 10"><path d="M2 4l1.5-2h3L8 4 5 8z" fill="#fff"/></svg></div><h4>Lifetime Savings</h4><p>Lorem ipsum dolor sit amet, etur adipiscing elit,</p></div>
    <a class="abs btn" style="left:277px;top:954px">LEARN MORE</a>
  </section>

  <section>
    <div class="abs band"></div>
    <h2 class="abs section-title band-title">Client Testimonials</h2>
    <article class="abs tcard" style="left:44px"><div class="avatar" role="img" aria-label="Client portrait"></div><h4>John Doe</h4><p>Lorem ipsum dolor sit amet, consectetur adipiscing elit, sed do eiusmod tempor incididunt ut labore et dolore.</p></article>
    <article class="abs tcard" style="left:203px"><div class="avatar" role="img" aria-label="Client portrait"></div><h4>Mara L</h4><p>Lorem ipsum dolor sit amet, consectetur adipiscing elit, sed do eiusmod tempor incididunt ut labore et dolore.</p></article>
    <article class="abs tcard" style="left:362px"><div class="avatar" role="img" aria-label="Client portrait"></div><h4>Ines K</h4><p>Lorem ipsum dolor sit amet, consectetur adipiscing elit, sed do eiusmod tempor incididunt ut labore et dolore.</p></article>
    <div class="abs dots"><i></i><i class="on"></i><i></i></div>
  </section>

  <section>
    <h2 class="abs section-title" style="top:1394px">Our Project</h2>
    <div class="abs proj" style="left:52px;background:linear-gradient(#e7e7e7,#5a5a5a)" role="img" aria-label="Lift lobby interior"></div>
    <div class="abs proj" style="left:168px;background:linear-gradient(#d9dde0,#8c7560)" role="img" aria-label="Bright corridor with wood panels"></div>
    <div class="abs proj" style="left:283px;background:linear-gradient(#6a5a3a,#8a4030)" role="img" aria-label="Hotel hallway with guests"></div>
    <div class="abs proj" style="left:398px;background:linear-gradient(#6f7f92,#3d4450)" role="img" aria-label="Lounge interior with tall windows"></div>
  </section>

  <section>
    <h2 class="abs contact-title">Contact Us</h2>
    <div class="abs label" style="left:54px;top:1600px">Full name <b>*</b></div>
    <div class="abs label" style="left:217px;top:1600px">Email Address <b>*</b></div>
    <div class="abs field" style="left:52px;top:1616px;width:152px;height:32px">Full name</div>
    <div class="abs field" style="left:216px;top:1616px;width:152px;height:32px">Email</div>
    <div class="abs label" style="left:54px;top:1659px">Message <b>*</b></div>
    <div class="abs field" style="left:52px;top:1676px;width:314px;height:69px">Message</div>
    <a class="abs btn" style="left:52px;top:1755px;font-size:8px">SUBMIT</a>
    <div class="abs map" role="img" aria-label="Street map showing office locations"></div>
  </section>

  <footer class="abs footer">
    <div class="abs f-brand"><span class="dot"></span>DUNMORE RIDGE<br>CONSTRUCTION</div>
    <div class="abs vline" style="left:169px"></div>
    <div class="abs vline" style="left:281px"></div>
    <div class="abs vline" style="left:392px"></div>
    <div class="abs" style="left:186px;top:22px;width:90px">
      <div class="f-head">Contact</div>
      <div class="f-row" style="margin-top:8px"><span class="pin"></span><span class="f-small">Alder Row 14 Eastfield<br>Valley 40-118</span></div>
      <div class="f-row" style="margin-top:8px"><span class="pin"></span><span class="f-small">(+00) 555 01 234</span></div>
      <div class="f-row" style="margin-top:10px"><span class="pin"></span><span class="f-small">hello (at) dunmoreridge</span></div>
    </div>
    <div class="abs" style="left:302px;top:24px">
      <div class="f-head">Quick Link</div>
      <div class="links" style="margin-top:4px"><div style="color:var(--blue)">Home</div><div>Service</div><div>Portfolio</div><div>Contact Us</div></div>
    </div>
    <div class="abs" style="left:413px;top:24px">
      <div class="f-head">Follow Us</div>
      <div class="f-small" style="margin-top:6px">Visit &amp; Follow Dunmore Ridge<br>at our social media account</div>
      <div class="socials"><i></i><i></i><i></i><i></i></div>
    </div>
  </footer>

</main>
</div>
</body>
</html>
```